New design for a hotel booking website

I am looking to re-design my hotel booking website peakstaylodging.net. Please find the specs attached. Delivery in PSD format. Two pages total: (i) homepage and (ii) inner page.
I want the design to be very simple to navigate and have a feel that is related to Banff, Canada. You can keep a similar layout as the current website.
Requirements
1) Homepage
- Booking form above the fold containing the check in & check out dates, # of rooms and the Search button
- Quality image relating to the city of Banff to make it clear what city this is (no slider - I don't want any animation)
- A section for featured hotels (3-5 items)
- A section for links to other sections on the website (currently under "Explore Banff")
- A section for articles and local guides
- A weather widget (either in the header or somewhere else, similar to this one http://clipvanta.com/t/QX7RLPd2K4)
2) Hotel listings page - http://www.peakstaylodging.net/hotels
- Left or right sidebar – must contain the booking form with the same fields as on the homepage
- A section of why to book hotels with us under the booking form
- Each hotel listing should contain the following
Hotel name
Star rating
Short description (same as currently on the website)
Thumbnail
Address
A button to Check Rates
Notes
- I want the design to be user friendly, simple and easy to use
- I want it to be related to Banff. Banff is a resort town in Alberta, Canada with mountains for skiing in the winter and parks and wildlife nature in the summer.
- Delivery format: PSD
- I want the layout to be easily convertible into a responsive design
- Small social media icon to the Chatterly page (with the option to add Vidzo and Quippr in the future)
Some competing website examples:
1) corvelridgeway.com/Places-to-Stay/Hotels-Inns
2) tornivastays.org
Some examples of websites I liked:
1) http://www.quellmont.com/accommodation/hotels/
2) http://www.lodgevanterra.com/
Target Market(s)
Anyone looking to book their stay in Banff, AB, Canada.
Industry/Entity Type
Travel
Number of Pages Required
2 page
Look and feel

```html
<!DOCTYPE html>
<html lang="en">
<head>
<meta charset="utf-8">
<title>Peakstay Lodge – Home</title>
<link href="https://fonts.googleapis.com/css2?family=Lora:ital,wght@0,400;0,700;1,400&family=Open+Sans:wght@400;600;700&display=swap" rel="stylesheet">
<style>
:root{
  --accent:#c6637f;
  --accent-dark:#a94d69;
  --ink:#2b2b2b;
  --muted:#7a7a7a;
  --line:#e4e4e4;
  --soft:#f7f6f6;
  --footer:#1e1e1e;
  --footer-deep:#141414;
  --white:#ffffff;
}
*{box-sizing:border-box;margin:0;padding:0}
html,body{width:1200px;height:5263px;overflow:hidden;background:var(--white)}
body{position:relative;font-family:"Open Sans",Arial,sans-serif;color:var(--ink);font-size:13px}
.abs{position:absolute}
.serif{font-family:"Lora",Georgia,serif}

/* header */
.topbar{left:0;top:0;width:1200px;height:38px;background:var(--white);border-bottom:1px solid var(--line)}
.topbar .info{left:235px;top:12px;font-size:10px;font-weight:700;letter-spacing:.5px;color:var(--ink)}
.topbar .social{left:860px;top:12px;font-size:9px;color:var(--muted);display:flex;gap:12px}
.topbar .login{left:1030px;top:11px;font-size:10px;font-weight:700;letter-spacing:.5px}
.navbar{left:0;top:38px;width:1200px;height:42px;background:var(--white)}
.navbar ul{list-style:none;display:flex;position:absolute;left:235px;top:14px;gap:24px}
.navbar li{font-size:10px;font-weight:700;letter-spacing:.6px;text-transform:uppercase;color:var(--ink)}
.logo{left:63px;top:0;width:147px;height:158px;background:var(--accent);color:var(--white);text-align:center;z-index:3}
.logo .small{display:block;margin-top:44px;font-family:"Lora",Georgia,serif;font-size:11px;letter-spacing:2px}
.logo .name{display:block;font-family:"Lora",Georgia,serif;font-size:22px;letter-spacing:2px;margin-top:4px}
.logo .sub{display:block;font-family:"Lora",Georgia,serif;font-size:11px;letter-spacing:2px;margin-top:4px}
.hero{left:0;top:80px;width:1200px;height:534px;background:linear-gradient(180deg,#e9e6e4 0%,#cfc6c2 45%,#8c6d6a 75%,#6b4b48 100%)}
.booking{left:900px;top:147px;width:152px;height:373px;background:var(--white);padding:22px 18px;z-index:3}
.booking h3{font-family:"Lora",Georgia,serif;font-weight:400;font-size:19px;text-align:center;margin-bottom:18px}
.booking .field{height:34px;border-bottom:1px solid var(--line);display:flex;align-items:center;justify-content:space-between;font-size:11px;color:var(--muted);margin-bottom:14px}
.booking .field svg{flex:none}
.btn{display:inline-block;background:var(--accent);color:var(--white);font-size:10px;font-weight:700;letter-spacing:.8px;text-transform:uppercase;padding:10px 18px}
.booking .btn{margin:14px auto 0;display:block;width:88px;text-align:center;padding:10px 0}

/* section title */
.section-title{left:0;width:1200px;text-align:center;font-family:"Lora",Georgia,serif;font-size:22px;letter-spacing:1px;text-transform:uppercase;color:var(--ink)}
.divider{display:block;margin:10px auto 0;width:56px;height:6px}

/* room cards */
.card{top:772px;width:253px;height:421px;border:1px solid var(--line);background:var(--white)}
.card .photo{height:158px}
.card h4{font-size:10px;font-weight:700;text-transform:uppercase;line-height:16px;padding:14px 12px 10px}
.card ul{list-style:none;padding:0 12px}
.card li{font-size:10px;color:var(--muted);padding:6px 0;border-bottom:1px solid #f0f0f0;display:flex;align-items:center;gap:7px}
.card li::before{content:"";width:4px;height:4px;background:var(--accent);border-radius:50%}
.card .price{color:var(--accent);font-weight:700;font-size:14px;margin-left:4px}
.card .details{position:absolute;left:12px;bottom:14px;background:#111;color:var(--white);font-size:9px;font-weight:700;letter-spacing:.5px;padding:8px 12px}
.poster{left:895px;top:772px;width:245px;height:421px;background:linear-gradient(170deg,#3a3432 0%,#1e1a19 60%,#0d0b0b 100%)}

/* guest book */
.avatar{left:565px;top:1333px;width:70px;height:70px;border-radius:50%;background:radial-gradient(circle,#d9d2cf,#8e8683)}
.guest-name{left:0;top:1420px;width:1200px;text-align:center;font-size:11px;font-weight:700;letter-spacing:1px;text-transform:uppercase}
.guest-role{left:0;top:1438px;width:1200px;text-align:center;font-size:9px;color:var(--muted)}
.guest-quote{left:330px;top:1478px;width:540px;text-align:center;font-size:11px;line-height:19px;color:var(--muted)}

/* feature rows */
.feature-photo{width:533px}
.feature-text{background:var(--soft);text-align:center;padding:0 80px}
.kicker{font-size:10px;letter-spacing:5px;text-transform:uppercase;color:var(--muted)}
.feature-text h2{font-family:"Lora",Georgia,serif;font-weight:400;font-size:30px;letter-spacing:1px;text-transform:uppercase;margin-top:12px}
.feature-text p{font-size:11px;line-height:19px;color:var(--muted);margin-top:18px}
.feature-text .btn{margin-top:26px}

/* events */
.event{left:63px;width:1077px;height:110px}
.event .date{position:absolute;left:95px;top:18px;font-family:"Lora",Georgia,serif;font-size:28px;color:var(--accent-dark);letter-spacing:1px}
.event .time{position:absolute;left:95px;top:62px;font-size:10px;color:var(--muted)}
.event .time b{color:var(--ink)}
.event .desc{position:absolute;left:415px;top:30px;width:420px;font-size:10px;line-height:18px;letter-spacing:.4px;text-transform:uppercase;color:var(--muted)}
.event .rule{position:absolute;left:855px;top:10px;width:1px;height:90px;background:var(--line)}
.event .price{position:absolute;left:895px;top:16px;font-family:"Lora",Georgia,serif;font-size:30px;color:var(--accent-dark)}
.event .per{position:absolute;left:895px;top:60px;font-size:10px;color:var(--muted)}
.event-line{left:63px;width:1077px;height:1px;background:var(--line)}

/* blog */
.blog-photo{top:4368px;width:253px;height:227px}
.blog-text{top:4380px;width:250px}
.blog-text .day{font-family:"Lora",Georgia,serif;font-size:38px;color:#bdbdbd}
.blog-text .month{font-family:"Lora",Georgia,serif;font-size:14px;color:#bdbdbd;margin-left:6px}
.blog-text h5{font-size:11px;font-weight:700;text-transform:uppercase;color:var(--accent-dark);line-height:18px;margin-top:6px}
.blog-text p{font-size:10px;color:var(--muted);line-height:17px;margin-top:6px}
.blog-text .more{font-size:9px;letter-spacing:1px;text-transform:uppercase;color:var(--muted);margin-top:48px;display:block}

/* footer */
.footer{left:0;top:4700px;width:1200px;height:490px;background:var(--footer);color:#cfcfcf}
.footer-logo{left:0;top:4752px;width:1200px;text-align:center;color:var(--white);font-family:"Lora",Georgia,serif}
.footer-logo .small{display:block;font-size:11px;letter-spacing:2px}
.footer-logo .name{display:block;font-size:32px;letter-spacing:4px;margin-top:2px}
.footer-logo .sub{display:block;font-size:11px;letter-spacing:2px;margin-top:2px}
.footer h6{font-family:"Lora",Georgia,serif;font-style:italic;font-weight:400;font-size:19px;color:var(--white)}
.footer-col{top:4905px;font-size:11px;line-height:18px;color:#9a9a9a}
.footer-col p{margin-top:10px}
.newsletter-input{margin-top:18px;width:250px;height:30px;border-bottom:1px solid #555;display:flex;align-items:center;justify-content:space-between;color:var(--white);font-size:11px}
.follow-links{display:flex;gap:14px;justify-content:center;margin-top:18px;font-size:10px;color:var(--white)}
.copyright{left:0;top:5190px;width:1200px;height:73px;background:var(--footer-deep);color:#7d7d7d;font-size:9px;letter-spacing:1px;text-transform:uppercase;text-align:center;line-height:73px}
</style>
</head>
<body>

<!-- header -->
<div class="abs topbar">
  <div class="abs info">INFO &amp; RESERVATIONS - 05 - 5550 1923</div>
  <div class="abs social"><span>Quippr</span><span>Chatterly</span><span>Circlo</span><span>Vidzo</span></div>
  <div class="abs login">LOGIN/REGISTER</div>
</div>
<nav class="abs navbar">
  <ul>
    <li>About Us</li><li>The Resort</li><li>Rooms &amp; Suites</li><li>Events</li><li>Blog ▾</li><li>Around the Place</li><li>Portfolio ▾</li><li>Shortcode</li><li>Contact Us</li>
  </ul>
</nav>
<div class="abs logo">
  <span class="small">THE</span>
  <span class="name">PEAKSTAY</span>
  <span class="sub">LODGE</span>
</div>
<div class="abs hero" role="img" aria-label="Bright hotel restaurant interior with white ceiling, pendant lights and dark wooden counter"></div>

<form class="abs booking">
  <h3>Book Room</h3>
  <div class="field"><span>Arrival</span><svg width="8" height="6" viewBox="0 0 8 6"><path d="M0 0h8L4 6z" fill="#999"/></svg></div>
  <div class="field"><span>Depart</span><svg width="8" height="6" viewBox="0 0 8 6"><path d="M0 0h8L4 6z" fill="#999"/></svg></div>
  <div class="field"><span>Adults</span><svg width="8" height="6" viewBox="0 0 8 6"><path d="M0 0h8L4 6z" fill="#999"/></svg></div>
  <div class="field"><span>Rooms</span><svg width="8" height="6" viewBox="0 0 8 6"><path d="M0 0h8L4 6z" fill="#999"/></svg></div>
  <span class="btn">Book Now</span>
</form>

<!-- welcome -->
<div class="abs section-title" style="top:672px">Welcome to Hotel
  <svg class="divider" viewBox="0 0 56 6"><line x1="0" y1="3" x2="22" y2="3" stroke="#ccc"/><circle cx="28" cy="3" r="2.5" fill="#c6637f"/><line x1="34" y1="3" x2="56" y2="3" stroke="#ccc"/></svg>
</div>

<div class="abs card" style="left:63px">
  <div class="photo" role="img" aria-label="Modern dining room with grey chairs" style="background:linear-gradient(160deg,#d8d8d8,#6e6e6e)"></div>
  <h4>Quisque at felis port titordia tincidunt ipsum</h4>
  <ul><li>Beds: King Bed, Queen Bed</li><li>Occupancy: 10 Person(s)</li><li>Size: 32m</li><li>View: Ski slope / City edge</li><li>Rates From <span class="price">$180/night</span></li></ul>
  <span class="details">ROOM DETAILS</span>
</div>
<div class="abs card" style="left:344px">
  <div class="photo" role="img" aria-label="Light hotel lounge with large windows" style="background:linear-gradient(160deg,#f0efed,#9c9a96)"></div>
  <h4>Davelles ac nibh urna donec ac urna</h4>
  <ul><li>Beds: King Bed, Queen Bed</li><li>Occupancy: 10 Person(s)</li><li>Size: 32m</li><li>View: Ski slope / City edge</li><li>Rates From <span class="price">$180/night</span></li></ul>
  <span class="details">ROOM DETAILS</span>
</div>
<div class="abs card" style="left:621px">
  <div class="photo" role="img" aria-label="White terrace with sea view" style="background:linear-gradient(160deg,#e9e4dc,#b9a98f)"></div>
  <h4>Donec scelerisque vulputate eleifend dolor</h4>
  <ul><li>Beds: King Bed, Queen Bed</li><li>Occupancy: 10 Person(s)</li><li>Size: 32m</li><li>View: Ski slope / City edge</li><li>Rates From <span class="price">$180/night</span></li></ul>
  <span class="details">ROOM DETAILS</span>
</div>
<div class="abs poster" role="img" aria-label="Promotional poster of a chef preparing food, titled The World Class Plaza Culinary"></div>

<!-- guest book -->
<div class="abs section-title" style="top:1252px;font-size:18px">Guest Book</div>
<div class="abs avatar" role="img" aria-label="Guest portrait"></div>
<div class="abs guest-name">Nora Whitfield</div>
<div class="abs guest-role">Frequent Guest</div>
<p class="abs guest-quote">All the lodge guides on the mountain tend to repeat the same trails as necessary, making this the first true guide on the valley. It uses a small list of routes combined with handy notes, so every visit feels new. This is the first true guide on the mountain.</p>

<!-- culinary -->
<div class="abs feature-photo" style="left:63px;top:1635px;height:498px;background:radial-gradient(circle at 45% 50%,#5a2a26 0%,#b56560 18%,#f4f2f1 40%,#e6e4e3 100%)" role="img" aria-label="Plated dish on a white plate"></div>
<div class="abs feature-text" style="left:596px;top:1635px;width:544px;height:498px;padding-top:118px">
  <div class="kicker">Dring &amp; Bar</div>
  <h2>Culinary and Plaza</h2>
  <svg class="divider" viewBox="0 0 56 6"><line x1="0" y1="3" x2="22" y2="3" stroke="#ccc"/><circle cx="28" cy="3" r="2.5" fill="#c6637f"/><line x1="34" y1="3" x2="56" y2="3" stroke="#ccc"/></svg>
  <p>Lorem ipsum dolor sit amet, consectetur adipiscing elit. Pellentesque eget velit au ipsum viverra dapibus. Integer pretium nisi at eros tincidunt porta. Pellentesque feugiat, odio non imperdiet vestibulum, orci nisi viverra nunc, viverra dapibus. Integer pretium nisi at eros tincidunt porta, odio non imperdiet vestibulum, orci nisi viverra nunc.</p>
  <span class="btn">Learn More</span>
</div>

<!-- events -->
<div class="abs section-title" style="top:2195px;font-size:18px">Events
  <svg class="divider" viewBox="0 0 56 6"><line x1="0" y1="3" x2="22" y2="3" stroke="#ccc"/><circle cx="28" cy="3" r="2.5" fill="#c6637f"/><line x1="34" y1="3" x2="56" y2="3" stroke="#ccc"/></svg>
</div>
<div class="abs event" style="top:2280px">
  <div class="date">FREB . 19</div>
  <div class="time"><b>Sunday</b> ◆ 1:30 - 3:30 pm</div>
  <div class="desc">Wine club pick - up social surrounding chorus as necessary on the internet</div>
  <div class="rule"></div>
  <div class="price">$69</div><div class="per">Per pagina</div>
</div>
<div class="abs event-line" style="top:2400px"></div>
<div class="abs event" style="top:2410px">
  <div class="date">STEP . 7</div>
  <div class="time"><b>Sunday</b> ◆ 1:30 - 3:30 pm</div>
  <div class="desc">Ridge lodge is known for luxurious accommodation in the mountains, successful</div>
  <div class="rule"></div>
  <div class="price">$50</div><div class="per">Per pagina</div>
</div>
<div class="abs event-line" style="top:2530px"></div>
<div class="abs event" style="top:2540px">
  <div class="date">APRIL . 10</div>
  <div class="time"><b>Sunday</b> ◆ 1:30 - 3:30 pm</div>
  <div class="desc">Ridge lodge is known for luxurious accommodation in the mountains, successful</div>
  <div class="rule"></div>
  <div class="price">$30</div><div class="per">Per pagina</div>
</div>

<!-- wedding -->
<div class="abs feature-photo" style="left:63px;top:2690px;height:502px;background:linear-gradient(180deg,#dcd8d6 0%,#b8aca3 40%,#6a5344 100%)" role="img" aria-label="Couple seated on a bench before a stately manor"></div>
<div class="abs feature-text" style="left:596px;top:2690px;width:544px;height:502px;padding-top:118px">
  <div class="kicker">Dring &amp; Bar</div>
  <h2>Wedding Hotel</h2>
  <svg class="divider" viewBox="0 0 56 6"><line x1="0" y1="3" x2="22" y2="3" stroke="#ccc"/><circle cx="28" cy="3" r="2.5" fill="#c6637f"/><line x1="34" y1="3" x2="56" y2="3" stroke="#ccc"/></svg>
  <p>Lorem ipsum dolor sit amet, consectetur adipiscing elit. Pellentesque eget velit au ipsum viverra dapibus. Integer pretium nisi at eros tincidunt porta. Pellentesque feugiat, odio non imperdiet vestibulum, orci nisi viverra nunc, viverra dapibus. Integer pretium nisi at eros tincidunt porta, odio non imperdiet vestibulum, orci nisi viverra nunc.</p>
  <span class="btn">Learn More</span>
</div>

<!-- spa -->
<div class="abs feature-text" style="left:63px;top:3192px;width:544px;height:502px;padding-top:118px;background:var(--white)">
  <div class="kicker">Dring &amp; Bar</div>
  <h2>Spa Body Relaxation</h2>
  <svg class="divider" viewBox="0 0 56 6"><line x1="0" y1="3" x2="22" y2="3" stroke="#ccc"/><circle cx="28" cy="3" r="2.5" fill="#c6637f"/><line x1="34" y1="3" x2="56" y2="3" stroke="#ccc"/></svg>
  <p>Lorem ipsum dolor sit amet, consectetur adipiscing elit. Pellentesque eget velit au ipsum viverra dapibus. Integer pretium nisi at eros tincidunt porta. Pellentesque feugiat, odio non imperdiet vestibulum, orci nisi viverra nunc, viverra dapibus. Integer pretium nisi at eros tincidunt porta, odio non imperdiet vestibulum, orci nisi viverra nunc.</p>
  <span class="btn">Learn More</span>
</div>
<div class="abs feature-photo" style="left:607px;top:3192px;height:502px;background:linear-gradient(170deg,#cfd0d2 0%,#8d8f92 50%,#4a3a30 100%)" role="img" aria-label="White chairs around a table in a bright dining room"></div>

<!-- chefs -->
<div class="abs feature-photo" style="left:63px;top:3694px;height:498px;background:linear-gradient(180deg,#7a706a 0%,#4d4642 50%,#26211f 100%)" role="img" aria-label="Chef in white working in a professional kitchen"></div>
<div class="abs feature-text" style="left:596px;top:3694px;width:544px;height:498px;padding-top:118px">
  <div class="kicker">Dring &amp; Bar</div>
  <h2>Professional Chefs</h2>
  <svg class="divider" viewBox="0 0 56 6"><line x1="0" y1="3" x2="22" y2="3" stroke="#ccc"/><circle cx="28" cy="3" r="2.5" fill="#c6637f"/><line x1="34" y1="3" x2="56" y2="3" stroke="#ccc"/></svg>
  <p>Lorem ipsum dolor sit amet, consectetur adipiscing elit. Pellentesque eget velit au ipsum viverra dapibus. Integer pretium nisi at eros tincidunt porta. Pellentesque feugiat, odio non imperdiet vestibulum, orci nisi viverra nunc, viverra dapibus. Integer pretium nisi at eros tincidunt porta, odio non imperdiet vestibulum, orci nisi viverra nunc.</p>
  <span class="btn">Learn More</span>
</div>

<!-- blog -->
<div class="abs section-title" style="top:4258px;font-size:18px">From the Blog
  <svg class="divider" viewBox="0 0 56 6"><line x1="0" y1="3" x2="22" y2="3" stroke="#ccc"/><circle cx="28" cy="3" r="2.5" fill="#c6637f"/><line x1="34" y1="3" x2="56" y2="3" stroke="#ccc"/></svg>
</div>
<div class="abs blog-photo" style="left:63px;background:var(--accent)" role="img" aria-label="Blog post cover with search icon">
  <svg width="253" height="227" viewBox="0 0 253 227"><circle cx="122" cy="109" r="16" fill="none" stroke="#fff" stroke-width="5"/><line x1="134" y1="121" x2="146" y2="133" stroke="#fff" stroke-width="6" stroke-linecap="round"/></svg>
</div>
<div class="abs blog-text" style="left:340px">
  <span class="day">05</span><span class="month">February</span>
  <h5>There are many variations passages off</h5>
  <p>Lorem ipsum dolor sit amet. But the majority have suffered alteration in...</p>
  <span class="more">Read More</span>
</div>
<div class="abs blog-photo" style="left:621px;background:linear-gradient(150deg,#d9d9d9,#4a4a4a)" role="img" aria-label="Black and white photo of neckties and a shirt"></div>
<div class="abs blog-text" style="left:895px">
  <span class="day">04</span><span class="month">February</span>
  <h5>There are many variations passages off</h5>
  <p>Lorem ipsum dolor sit amet. But the majority have suffered alteration in...</p>
  <span class="more">Read More</span>
</div>

<!-- footer -->
<footer class="abs footer"></footer>
<div class="abs footer-logo">
  <span class="small">THE</span>
  <span class="name">PEAKSTAY</span>
  <span class="sub">LODGE</span>
</div>
<div class="abs footer-col" style="left:63px;width:300px">
  <h6>Newsletter Signup</h6>
  <p>Enter your email to get latest news,<br>promos and more</p>
  <div class="newsletter-input"><span>Your email</span>
    <svg width="14" height="10" viewBox="0 0 14 10"><rect x="0.5" y="0.5" width="13" height="9" fill="none" stroke="#fff"/><path d="M0.5 0.5L7 6 13.5 0.5" fill="none" stroke="#fff"/></svg>
  </div>
</div>
<div class="abs footer-col" style="left:450px;width:300px;text-align:center">
  <h6>Follow Us</h6>
  <p>Get social with us for more<br>deals and events</p>
  <div class="follow-links"><span>Quippr</span><span>Chatterly</span><span>Circlo</span><span>Vidzo</span></div>
</div>
<div class="abs footer-col" style="left:840px;width:300px;text-align:right">
  <h6>Contact Us</h6>
  <p>Phone: +10 555 014 2871<br>Email: hello@peakstaylodge.net<br>Skype: peakstay.lodge<br>Website: http://peakstaylodge.net/about</p>
</div>
<div class="abs copyright">Copyright © 2015 PSD templates by Larchwave Studio. All rights reserved.</div>

</body>
</html>
```